Door Hanger Design for Electricians Serving Homes

I would like our logo incorporated into the door hanger. We would like a place for a tear off section on the bottom of the hanger with our contact information: K&T Electric - (555) 318-4702 - www.kandtelectric.example - info@kandtelectric.example.
Door Hanger Script
Front Side of the Door Hanger:
[Company Logo]
Need a Reliable Electrician?
Your Local Electrical Expert is Just Around the Corner!
• Quick Response Times
• Affordable Rates
• Quality Workmanship
• Fully Licensed & Insured
• Special Offer:
• 10% OFF Your First Service Call!
Back Side of the Door Hanger:
Don't Let Electrical Issues Keep You in the Dark!
From flickering lights to complete system upgrades, we've got all your
residential electrical needs covered. Our services include:
• Electrical Repairs & Troubleshooting
• Lighting Installation & Upgrades
• Safety Inspections & Code Compliance
• Energy-Efficient Solutions
• 24/7 Emergency Services
• Why Choose Us?
• Friendly, Local Service
• Over 30 Years of Experience
• Satisfaction Guaranteed
• Upfront Pricing
Call Us Today: [Your Phone Number]
Visit Our Website: [Your Website]
Book Your Appointment Now and Claim Your 10% Discount!
Offer valid for new customers on the first visit only. Mention this door hanger when
booking.
[Your Company Name and Contact Information]
Follow Us on Social Media for More Tips and Special Offers!
[Icons for social media platforms: Chatterpage, Pixmosaic, Quibbler, etc.]
Design Tips:
Use bold, clear fonts for easy reading.
Incorporate your brand colors and logo for instant recognition.
Include a clear call to action (CTA) on both sides.
Add a tear-off section at the bottom with your contact information for
convenience.
Use high-quality images or graphics related to electrical work to catch
the eye.
This door hanger design and copy aim to attract residential clients by
highlighting the benefits of your electrical services, special offers, and
how they can easily get in touch with you for their electrical needs.
The door knocker template will have three of the same design on front and three of the same design on the back. This template is from the print shop.

```html
<!DOCTYPE html>
<html lang="en">
<head>
<meta charset="utf-8">
<title>K&amp;T Electric Door Hangers</title>
<link rel="stylesheet" href="https://fonts.googleapis.com/css2?family=Montserrat:wght@700;800;900&family=Lato:wght@400;700;900&display=swap">
<style>
  :root {
    --sheet: #ededed;
    --ink: #000000;
    --paper: #ffffff;
    --red: #d40c0c;
    --text: #111111;
  }
  * { box-sizing: border-box; margin: 0; padding: 0; }
  html, body { width: 960px; height: 1200px; overflow: hidden; background: var(--sheet); }
  body { position: relative; font-family: "Lato", Arial, sans-serif; color: var(--text); }

  .hanger { position: absolute; width: 209px; height: 489px; background: var(--paper); overflow: hidden; }
  .col-1 { left: 96px; } .col-2 { left: 376px; } .col-3 { left: 656px; }
  .row-front { top: 85px; } .row-back { top: 626px; }

  .photo { position: absolute; left: 0; top: 0; width: 209px; }
  .front .photo { height: 158px; }
  .back .photo { height: 116px; }
  .photo-lamps { background: radial-gradient(circle at 40% 40%, #e8d3a4 0%, #9c7f4e 30%, #1d1a15 70%); }
  .photo-chandelier { background: radial-gradient(circle at 55% 35%, #e9dcc2 0%, #8c7a5e 35%, #384456 75%); }
  .photo-bulbs { background: radial-gradient(circle at 55% 45%, #f0a84a 0%, #a5541a 30%, #1a0d05 70%); }
  .photo-panel { background: linear-gradient(135deg, #8d939a 0%, #4a4c50 45%, #2a2a2a 70%, #c9b23a 100%); }
  .photo-technician { background: linear-gradient(120deg, #b83232 0%, #24416e 45%, #d27c4e 70%, #1b2f52 100%); }
  .photo-bar { background: linear-gradient(180deg, #6d6e74 0%, #a49e94 50%, #d8d6d2 80%, #8a6a4a 100%); }

  .die-cut { position: absolute; left: 0; top: 0; width: 209px; height: 116px; }

  .brand-name { position: absolute; font-family: "Montserrat", Arial, sans-serif; font-weight: 800; font-size: 13px; line-height: 1; }
  .brand-photo { left: 22px; top: 132px; color: var(--paper); }
  .brand-paper { color: var(--ink); }

  .headline-band { position: absolute; left: 0; width: 209px; background: var(--ink); color: var(--paper);
    font-family: "Montserrat", Arial, sans-serif; font-weight: 900; text-align: center; display: flex; align-items: center; justify-content: center; }
  .front .headline-band { top: 158px; height: 64px; font-size: 21px; line-height: 1.05; }
  .back .headline-band { top: 116px; height: 72px; font-size: 18.5px; line-height: 1.0; }

  .tagline { position: absolute; left: 0; top: 233px; width: 209px; text-align: center; font-family: "Montserrat", Arial, sans-serif; font-weight: 700; font-size: 12px; line-height: 1.25; }

  .worker-photo { position: absolute; left: 118px; top: 275px; width: 91px; height: 160px;
    background: linear-gradient(90deg, rgba(255,255,255,1) 0%, #c7d3dc 25%, #3a52a0 55%, #a9b8c6 100%); }
  .detail-photo { position: absolute; left: 136px; top: 288px; width: 73px; height: 88px; }
  .detail-bulbs-light { background: radial-gradient(circle at 50% 55%, #f3c48a 0%, #b58a62 35%, #e8e0d6 75%); }
  .detail-bulbs-dark { background: radial-gradient(circle at 50% 45%, #f6b24a 0%, #7a3c10 40%, #120a04 80%); }
  .detail-panel { background: linear-gradient(160deg, #3a6ea8 0%, #d9dde2 40%, #f4f4f4 70%, #9aa4ae 100%); }

  .bullets { position: absolute; left: 14px; list-style: none; font-size: 9px; line-height: 11.6px; }
  .front .bullets { top: 279px; }
  .back .bullets { top: 253px; }
  .bullets li { display: flex; align-items: center; gap: 2px; white-space: nowrap; }
  .bullets svg { width: 6px; height: 7px; flex: none; }

  .offer { position: absolute; left: 23px; top: 340px; font-weight: 900; font-size: 9px; line-height: 1.15; }
  .offer .deal { color: var(--red); font-family: "Montserrat", Arial, sans-serif; font-size: 13px; font-weight: 800; line-height: 1; display: block; }
  .front .brand-paper { left: 23px; top: 396px; }

  .intro { position: absolute; left: 0; top: 199px; width: 209px; text-align: center; font-weight: 900; font-size: 9.4px; line-height: 1.2; }
  .services-title { position: absolute; left: 0; top: 237px; width: 209px; text-align: center; color: var(--red); font-weight: 900; font-size: 9.4px; }
  .why { position: absolute; left: 18px; top: 335px; font-weight: 900; font-size: 8.6px; line-height: 1.35; }
  .back .brand-paper { left: 16px; top: 386px; width: 54px; font-size: 11px; line-height: 1.15; }
  .booking { position: absolute; left: 75px; top: 380px; font-weight: 900; font-size: 8.4px; line-height: 1.45; white-space: nowrap; }
  .booking .deal { color: var(--red); font-family: "Montserrat", Arial, sans-serif; font-weight: 800; font-size: 12px; }
  .fine-print { position: absolute; left: 73px; top: 408px; font-size: 4.6px; line-height: 1.4; white-space: nowrap; }

  .call-pill { position: absolute; left: 50%; transform: translateX(-50%); top: 425px; height: 17px; padding: 0 5px;
    background: var(--red); color: var(--paper); border-radius: 9px; font-family: "Montserrat", Arial, sans-serif; font-weight: 700;
    font-size: 11px; line-height: 17px; white-space: nowrap; z-index: 2; }
  .contact-band { position: absolute; left: 0; top: 434px; width: 209px; height: 55px; background: var(--ink); color: var(--paper); text-align: center; }
  .phone { position: absolute; left: 0; top: 8px; width: 100%; font-family: "Montserrat", Arial, sans-serif; font-weight: 700; font-size: 16px; line-height: 1; }
  .visit { position: absolute; left: 0; top: 26px; width: 100%; font-size: 6.5px; line-height: 1; }
  .website { position: absolute; left: 0; top: 34px; width: 100%; font-family: "Montserrat", Arial, sans-serif; font-weight: 700; font-size: 11px; line-height: 1.2; }
</style>
</head>
<body>

<!-- Front row -->
<section class="hanger front row-front col-1">
  <div class="photo photo-lamps" role="img" aria-label="Warm glowing square pendant lamps against a dark ceiling"></div>
  <svg class="die-cut" viewBox="0 0 209 116" aria-hidden="true"><g fill="none" stroke="#fff" stroke-width="0.8" stroke-dasharray="4 3"><line x1="40" y1="0" x2="84" y2="44"/><circle cx="105" cy="65" r="29"/></g></svg>
  <div class="brand-name brand-photo">K&amp;T Electric</div>
  <h1 class="headline-band">Need a Reliable<br>Electrician?</h1>
  <p class="tagline">Your Local Electrical Expert<br>is Just Around the Corner!</p>
  <div class="worker-photo" role="img" aria-label="Smiling electrician in hard hat and blue overalls carrying cable"></div>
  <ul class="bullets">
    <li><svg viewBox="0 0 6 7"><polygon points="0,0 6,3.5 0,7 2,3.5" fill="#d40c0c"/></svg>Quick Response Times</li>
    <li><svg viewBox="0 0 6 7"><polygon points="0,0 6,3.5 0,7 2,3.5" fill="#d40c0c"/></svg>Affordable Rates</li>
    <li><svg viewBox="0 0 6 7"><polygon points="0,0 6,3.5 0,7 2,3.5" fill="#d40c0c"/></svg>Quality Workmanship</li>
    <li><svg viewBox="0 0 6 7"><polygon points="0,0 6,3.5 0,7 2,3.5" fill="#d40c0c"/></svg>Fully Licensed &amp; Insured</li>
  </ul>
  <p class="offer">Special Offer:<span class="deal">10% OFF</span>Your First Service Call!</p>
  <div class="brand-name brand-paper">K&amp;T Electric</div>
  <div class="call-pill">Call Us Today</div>
  <footer class="contact-band"><div class="phone">(555) 318-4702</div><div class="visit">Visit Our Website:</div><div class="website">www.kandtelectric.example</div></footer>
</section>

<section class="hanger front row-front col-2">
  <div class="photo photo-chandelier" role="img" aria-label="Modern crystal chandelier hanging from a recessed ceiling"></div>
  <svg class="die-cut" viewBox="0 0 209 116" aria-hidden="true"><g fill="none" stroke="#fff" stroke-width="0.8" stroke-dasharray="4 3"><line x1="40" y1="0" x2="84" y2="44"/><circle cx="105" cy="65" r="29"/></g></svg>
  <div class="brand-name brand-photo">K&amp;T Electric</div>
  <h1 class="headline-band">Need a Reliable<br>Electrician?</h1>
  <p class="tagline">Your Local Electrical Expert<br>is Just Around the Corner!</p>
  <div class="worker-photo" role="img" aria-label="Smiling electrician in hard hat and blue overalls carrying cable"></div>
  <ul class="bullets">
    <li><svg viewBox="0 0 6 7"><polygon points="0,0 6,3.5 0,7 2,3.5" fill="#d40c0c"/></svg>Quick Response Times</li>
    <li><svg viewBox="0 0 6 7"><polygon points="0,0 6,3.5 0,7 2,3.5" fill="#d40c0c"/></svg>Affordable Rates</li>
    <li><svg viewBox="0 0 6 7"><polygon points="0,0 6,3.5 0,7 2,3.5" fill="#d40c0c"/></svg>Quality Workmanship</li>
    <li><svg viewBox="0 0 6 7"><polygon points="0,0 6,3.5 0,7 2,3.5" fill="#d40c0c"/></svg>Fully Licensed &amp; Insured</li>
  </ul>
  <p class="offer">Special Offer:<span class="deal">10% OFF</span>Your First Service Call!</p>
  <div class="brand-name brand-paper">K&amp;T Electric</div>
  <div class="call-pill">Call Us Today</div>
  <footer class="contact-band"><div class="phone">(555) 318-4702</div><div class="visit">Visit Our Website:</div><div class="website">www.kandtelectric.example</div></footer>
</section>

<section class="hanger front row-front col-3">
  <div class="photo photo-bulbs" role="img" aria-label="Glowing vintage filament light bulbs in the dark"></div>
  <svg class="die-cut" viewBox="0 0 209 116" aria-hidden="true"><g fill="none" stroke="#fff" stroke-width="0.8" stroke-dasharray="4 3"><line x1="40" y1="0" x2="84" y2="44"/><circle cx="105" cy="65" r="29"/></g></svg>
  <div class="brand-name brand-photo">K&amp;T Electric</div>
  <h1 class="headline-band">Need a Reliable<br>Electrician?</h1>
  <p class="tagline">Your Local Electrical Expert<br>is Just Around the Corner!</p>
  <div class="worker-photo" role="img" aria-label="Smiling electrician in hard hat and blue overalls carrying cable"></div>
  <ul class="bullets">
    <li><svg viewBox="0 0 6 7"><polygon points="0,0 6,3.5 0,7 2,3.5" fill="#d40c0c"/></svg>Quick Response Times</li>
    <li><svg viewBox="0 0 6 7"><polygon points="0,0 6,3.5 0,7 2,3.5" fill="#d40c0c"/></svg>Affordable Rates</li>
    <li><svg viewBox="0 0 6 7"><polygon points="0,0 6,3.5 0,7 2,3.5" fill="#d40c0c"/></svg>Quality Workmanship</li>
    <li><svg viewBox="0 0 6 7"><polygon points="0,0 6,3.5 0,7 2,3.5" fill="#d40c0c"/></svg>Fully Licensed &amp; Insured</li>
  </ul>
  <p class="offer">Special Offer:<span class="deal">10% OFF</span>Your First Service Call!</p>
  <div class="brand-name brand-paper">K&amp;T Electric</div>
  <div class="call-pill">Call Us Today</div>
  <footer class="contact-band"><div class="phone">(555) 318-4702</div><div class="visit">Visit Our Website:</div><div class="website">www.kandtelectric.example</div></footer>
</section>

<!-- Back row -->
<section class="hanger back row-back col-1">
  <div class="photo photo-panel" role="img" aria-label="Gloved hands testing wires in an electrical panel"></div>
  <svg class="die-cut" viewBox="0 0 209 116" aria-hidden="true"><g fill="none" stroke="#fff" stroke-width="0.8" stroke-dasharray="4 3"><line x1="40" y1="0" x2="84" y2="44"/><circle cx="105" cy="65" r="29"/></g></svg>
  <h2 class="headline-band">Don't Let Electrical<br>Issues Keep<br>You in the Dark!</h2>
  <p class="intro">From flickering lights to complete<br>system upgrades, we've got all your<br>residential electrical needs covered.</p>
  <p class="services-title">Our services include:</p>
  <div class="detail-photo detail-bulbs-light" role="img" aria-label="Hanging filament bulbs against a light wall"></div>
  <ul class="bullets">
    <li><svg viewBox="0 0 6 7"><polygon points="0,0 6,3.5 0,7 2,3.5" fill="#d40c0c"/></svg>Electrical Repairs &amp; Troubleshooting</li>
    <li><svg viewBox="0 0 6 7"><polygon points="0,0 6,3.5 0,7 2,3.5" fill="#d40c0c"/></svg>Lighting Installation &amp; Upgrades</li>
    <li><svg viewBox="0 0 6 7"><polygon points="0,0 6,3.5 0,7 2,3.5" fill="#d40c0c"/></svg>Safety Inspections &amp; Code Compliance</li>
    <li><svg viewBox="0 0 6 7"><polygon points="0,0 6,3.5 0,7 2,3.5" fill="#d40c0c"/></svg>Energy-Efficient Solutions</li>
    <li><svg viewBox="0 0 6 7"><polygon points="0,0 6,3.5 0,7 2,3.5" fill="#d40c0c"/></svg>24/7 Emergency Services</li>
  </ul>
  <p class="why">Why Choose Us?<br>Friendly, Local Service<br>Over 30 Years of Experience</p>
  <div class="brand-name brand-paper">K&amp;T<br>Electric</div>
  <p class="booking">Book Your Appointment Now<br>and Claim Your <span class="deal">10% OFF</span></p>
  <p class="fine-print">Offer valid for new customers on the first visit only.<br>Mention this door hanger when booking.</p>
  <div class="call-pill">Call Us Today</div>
  <footer class="contact-band"><div class="phone">(555) 318-4702</div><div class="visit">Visit Our Website:</div><div class="website">www.kandtelectric.example</div></footer>
</section>

<section class="hanger back row-back col-2">
  <div class="photo photo-technician" role="img" aria-label="Electrician in orange hard hat working on wiring"></div>
  <svg class="die-cut" viewBox="0 0 209 116" aria-hidden="true"><g fill="none" stroke="#fff" stroke-width="0.8" stroke-dasharray="4 3"><line x1="40" y1="0" x2="84" y2="44"/><circle cx="105" cy="65" r="29"/></g></svg>
  <h2 class="headline-band">Don't Let Electrical<br>Issues Keep<br>You in the Dark!</h2>
  <p class="intro">From flickering lights to complete<br>system upgrades, we've got all your<br>residential electrical needs covered.</p>
  <p class="services-title">Our services include:</p>
  <div class="detail-photo detail-bulbs-dark" role="img" aria-label="Glowing filament bulbs in the dark"></div>
  <ul class="bullets">
    <li><svg viewBox="0 0 6 7"><polygon points="0,0 6,3.5 0,7 2,3.5" fill="#d40c0c"/></svg>Electrical Repairs &amp; Troubleshooting</li>
    <li><svg viewBox="0 0 6 7"><polygon points="0,0 6,3.5 0,7 2,3.5" fill="#d40c0c"/></svg>Lighting Installation &amp; Upgrades</li>
    <li><svg viewBox="0 0 6 7"><polygon points="0,0 6,3.5 0,7 2,3.5" fill="#d40c0c"/></svg>Safety Inspections &amp; Code Compliance</li>
    <li><svg viewBox="0 0 6 7"><polygon points="0,0 6,3.5 0,7 2,3.5" fill="#d40c0c"/></svg>Energy-Efficient Solutions</li>
    <li><svg viewBox="0 0 6 7"><polygon points="0,0 6,3.5 0,7 2,3.5" fill="#d40c0c"/></svg>24/7 Emergency Services</li>
  </ul>
  <p class="why">Why Choose Us?<br>Friendly, Local Service<br>Over 30 Years of Experience</p>
  <div class="brand-name brand-paper">K&amp;T<br>Electric</div>
  <p class="booking">Book Your Appointment Now<br>and Claim Your <span class="deal">10% OFF</span></p>
  <p class="fine-print">Offer valid for new customers on the first visit only.<br>Mention this door hanger when booking.</p>
  <div class="call-pill">Call Us Today</div>
  <footer class="contact-band"><div class="phone">(555) 318-4702</div><div class="visit">Visit Our Website:</div><div class="website">www.kandtelectric.example</div></footer>
</section>

<section class="hanger back row-back col-3">
  <div class="photo photo-bar" role="img" aria-label="Bright modern bar interior with pendant lighting"></div>
  <svg class="die-cut" viewBox="0 0 209 116" aria-hidden="true"><g fill="none" stroke="#fff" stroke-width="0.8" stroke-dasharray="4 3"><line x1="40" y1="0" x2="84" y2="44"/><circle cx="105" cy="65" r="29"/></g></svg>
  <h2 class="headline-band">Don't Let Electrical<br>Issues Keep<br>You in the Dark!</h2>
  <p class="intro">From flickering lights to complete<br>system upgrades, we've got all your<br>residential electrical needs covered.</p>
  <p class="services-title">Our services include:</p>
  <div class="detail-photo detail-panel" role="img" aria-label="Gloved hand working inside a breaker panel"></div>
  <ul class="bullets">
    <li><svg viewBox="0 0 6 7"><polygon points="0,0 6,3.5 0,7 2,3.5" fill="#d40c0c"/></svg>Electrical Repairs &amp; Troubleshooting</li>
    <li><svg viewBox="0 0 6 7"><polygon points="0,0 6,3.5 0,7 2,3.5" fill="#d40c0c"/></svg>Lighting Installation &amp; Upgrades</li>
    <li><svg viewBox="0 0 6 7"><polygon points="0,0 6,3.5 0,7 2,3.5" fill="#d40c0c"/></svg>Safety Inspections &amp; Code Compliance</li>
    <li><svg viewBox="0 0 6 7"><polygon points="0,0 6,3.5 0,7 2,3.5" fill="#d40c0c"/></svg>Energy-Efficient Solutions</li>
    <li><svg viewBox="0 0 6 7"><polygon points="0,0 6,3.5 0,7 2,3.5" fill="#d40c0c"/></svg>24/7 Emergency Services</li>
  </ul>
  <p class="why">Why Choose Us?<br>Friendly, Local Service<br>Over 30 Years of Experience</p>
  <div class="brand-name brand-paper">K&amp;T<br>Electric</div>
  <p class="booking">Book Your Appointment Now<br>and Claim Your <span class="deal">10% OFF</span></p>
  <p class="fine-print">Offer valid for new customers on the first visit only.<br>Mention this door hanger when booking.</p>
  <div class="call-pill">Call Us Today</div>
  <footer class="contact-band"><div class="phone">(555) 318-4702</div><div class="visit">Visit Our Website:</div><div class="website">www.kandtelectric.example</div></footer>
</section>

</body>
</html>
```